Brindle.vc needs a better website design!

We need a new and better website for Brindle.vc. We're a Canadian venture capital firm that invests in innovative entrepreneurs. We compete against the following websites: tollery.vc, quorbinvest.ca, gavelvc.com, and duskara.vc. We're a diverse group of partners and we're dedicated to the founders we invest in.
Updates

I don’t really like stock photos of random people as part of the website design…so please try to stay away from using those images. Thanks, Owen

Target Market(s)

Canadian entrepreneurs and investors

Industry/Entity Type

Venture capital, finance, investment, entrepreneurship

Coding

Coded - Design and coding required

Number of Pages Required

4 page

Font styles to use
Sans Serif

Colors

Designer to choose colors to be used in the design.

Requirements
Must have
• Clean crisp overall design. Fast and to the point.
Nice to have
• Check out www.brindle.vc - I did it myself and it is too basic and too wordy.
Should not have
• No stock images with random people in them! Not too wordy or with too many large images that are slow to load.

```html
<!DOCTYPE html>
<html lang="en">
<head>
<meta charset="utf-8">
<title>Brindle.vc — Venture Capital</title>
<link rel="stylesheet" href="https://fonts.googleapis.com/css2?family=Poppins:wght@400;500;600;700&family=Lato:wght@400;700&display=swap">
<style>
:root{
  --green:#7d9a31;
  --green-dark:#5f7d1f;
  --green-light:#93b03f;
  --ink:#2b2b2b;
  --body:#555;
  --grey-bar:#9a9a9a;
  --black:#000;
  --white:#fff;
}
*{margin:0;padding:0;box-sizing:border-box}
html,body{width:1200px;height:3847px;overflow:hidden}
body{position:relative;background:var(--white);font-family:'Lato',sans-serif;color:var(--body)}
.abs{position:absolute}
a{color:inherit;text-decoration:none}
.heading{font-family:'Poppins',sans-serif;font-weight:500;text-transform:uppercase}
.btn{position:absolute;display:flex;align-items:center;justify-content:center;border-radius:30px;font-family:'Poppins',sans-serif;font-weight:500;font-size:15px;text-transform:uppercase}

/* header */
.topbar{left:410px;top:0;width:790px;height:42px;background:var(--grey-bar);clip-path:polygon(0 0,100% 0,100% 100%,40px 100%)}
.topbar-item{top:0;height:42px;display:flex;align-items:center;gap:14px;color:var(--white);font-family:'Poppins',sans-serif;font-size:14px}
.topbar-icon{width:32px;height:32px;border-radius:50%;background:var(--green);display:flex;align-items:center;justify-content:center}
.topbar-sep{left:855px;top:8px;width:1px;height:26px;background:#ddd}
.brand{left:110px;top:44px;display:flex;align-items:center;gap:12px}
.brand-dot{width:40px;height:40px;border-radius:50%;background:var(--green)}
.brand-name{font-family:'Poppins',sans-serif;font-weight:600;font-size:28px;color:var(--green);letter-spacing:.5px}
.nav-link{top:88px;font-family:'Poppins',sans-serif;font-size:15px;color:#333;transform:translateX(-50%)}
.nav-link.active{color:var(--green)}
.login{left:967px;top:76px;width:121px;height:45px;background:var(--green);color:var(--white)}

/* hero */
.hero-art{left:0;top:149px;width:1200px;height:593px}
.hero-circle{left:654px;top:203px;width:418px;height:418px;border-radius:50%;background:rgba(125,154,49,.93);text-align:center;color:var(--white)}
.hero-welcome{position:absolute;left:0;top:105px;width:100%;font-family:'Poppins',sans-serif;font-size:33px;font-weight:400}
.hero-title{position:absolute;left:0;top:145px;width:100%;font-family:'Poppins',sans-serif;font-size:62px;font-weight:700;letter-spacing:1px}
.hero-text{position:absolute;left:0;top:234px;width:100%;font-size:15px;line-height:27px}
.hero-cta{left:785px;top:506px;width:154px;height:43px;background:var(--white);color:var(--green)}
.hero-next{left:1103px;top:428px}

/* looking for */
.look-frame{left:136px;top:809px;width:412px;height:412px;border-radius:50%;background:var(--green);padding:9px}
.look-photo{width:100%;height:100%;border-radius:50%;background:linear-gradient(135deg,#c9cfd6 0%,#8a96a3 45%,#3c434c 100%)}
.look-title{left:651px;top:852px;font-size:30px;color:var(--ink)}
.look-text{left:651px;top:911px;width:442px;font-size:15.6px;line-height:26.5px;color:var(--body)}
.look-cta{left:651px;top:1151px;width:155px;height:43px;background:var(--green);color:var(--white)}

/* investments */
.invest{left:0;top:1303px;width:1200px;height:900px;background:var(--green)}
.invest-title{left:0;top:1368px;width:1200px;text-align:center;font-size:30px;color:var(--white)}
.step{width:314px;height:309px;text-align:center;color:var(--white)}
.step.featured{background:var(--white);color:var(--ink)}
.step-icon{position:absolute;left:127px;top:24px;width:60px;height:60px}
.step-title{position:absolute;left:0;top:111px;width:100%;font-family:'Poppins',sans-serif;font-size:22px;font-weight:500}
.step-text{position:absolute;left:0;top:155px;width:100%;font-size:15px;line-height:27px}
.step.featured .step-text{color:var(--body)}
.step-more{position:absolute;left:0;top:251px;width:100%;text-align:center;font-family:'Poppins',sans-serif;font-size:15px;font-weight:600}
.step.featured .step-more{color:var(--green)}
.view-all{left:536px;top:2084px;width:128px;height:44px;background:var(--white);color:var(--green)}

/* portfolio */
.portfolio-title{left:0;top:2280px;width:1200px;text-align:center;font-size:30px;color:var(--ink);font-weight:600}
.company{width:174px;height:174px;border-radius:50%;background:var(--white);box-shadow:0 3px 12px rgba(0,0,0,.16);display:flex;align-items:center;justify-content:center;gap:8px;font-family:'Poppins',sans-serif;font-weight:600;font-size:24px;color:#3a3a3a}
.company-mark{width:14px;height:14px;border-radius:50%;background:#3a3a3a}
.slider-arrow{width:38px;height:38px;border-radius:50%;background:var(--white);box-shadow:0 2px 8px rgba(0,0,0,.18);display:flex;align-items:center;justify-content:center}

/* team */
.team-art{left:0;top:2810px;width:1200px;height:620px}
.footer-base{left:0;top:3420px;width:1200px;height:427px;background:var(--black)}
.team-title{left:0;top:2882px;width:1200px;text-align:center;font-size:30px;color:var(--white)}
.member{width:229px;text-align:center;color:var(--white)}
.member-photo{height:186px;background:linear-gradient(180deg,#f4f4f4 0%,#d9d9d9 100%)}
.member-name{margin-top:14px;font-family:'Poppins',sans-serif;font-size:20px;font-weight:500}
.member-role{font-size:14px;margin-top:2px;white-space:nowrap}
.member-links{display:flex;justify-content:center;gap:18px;margin-top:14px}
.member-links span{width:16px;height:16px;border-radius:50%;background:var(--white)}

/* footer */
.footer-brand{left:110px;top:3560px;display:flex;align-items:center;gap:12px}
.footer-brand .brand-dot{background:var(--white)}
.footer-brand .brand-name{color:var(--white);font-size:30px}
.footer-head{top:3498px;font-family:'Poppins',sans-serif;font-size:18px;font-weight:500;color:var(--white);text-transform:uppercase}
.footer-links{left:357px;top:3541px;font-size:15px;line-height:27px;color:var(--white);list-style:none}
.contact-row{left:478px;display:flex;gap:14px;font-size:15px;line-height:22px;color:var(--white)}
.follow-row{left:710px;display:flex;align-items:center;gap:16px;font-size:15px;color:var(--white)}
.follow-dot{width:31px;height:31px;border-radius:50%;border:2px solid var(--white)}
.news-input{left:861px;top:3548px;width:226px;height:40px;border-radius:20px;background:var(--white);font-size:12px;color:#999;padding:0 16px;display:flex;align-items:center}
.news-submit{left:861px;top:3599px;width:105px;height:41px;background:var(--green);color:var(--white)}
.copyright{left:0;top:3775px;width:1200px;text-align:center;font-size:14px;color:var(--white)}
</style>
</head>
<body>

<!-- Header -->
<div class="abs topbar"></div>
<div class="abs topbar-item" style="left:604px">
  <span class="topbar-icon"><svg width="14" height="10" viewBox="0 0 14 10"><rect x="0.5" y="0.5" width="13" height="9" fill="none" stroke="#fff"/><path d="M0.5 0.5 L7 5.5 L13.5 0.5" fill="none" stroke="#fff"/></svg></span>
  <span>Email:&nbsp; hello@brindle.vc</span>
</div>
<div class="abs topbar-sep"></div>
<div class="abs topbar-item" style="left:879px">
  <span class="topbar-icon"><svg width="14" height="14" viewBox="0 0 24 24"><path d="M6.6 10.8a15 15 0 0 0 6.6 6.6l2.2-2.2c.3-.3.7-.4 1-.2 1.1.4 2.3.6 3.6.6.6 0 1 .4 1 1V20c0 .6-.4 1-1 1C10.6 21 3 13.4 3 4c0-.6.4-1 1-1h3.5c.6 0 1 .4 1 1 0 1.3.2 2.5.6 3.6.1.3 0 .7-.2 1z" fill="#fff"/></svg></span>
  <span>Call:&nbsp; (555) 014 2290</span>
</div>

<a class="abs brand" href="#"><span class="brand-dot"></span><span class="brand-name">BRINDLE.VC</span></a>

<nav>
  <a class="abs nav-link active" style="left:379px" href="#">HOME</a>
  <a class="abs nav-link" style="left:498px" href="#">WHAT</a>
  <a class="abs nav-link" style="left:618px" href="#">HOW</a>
  <a class="abs nav-link" style="left:730px" href="#">WHO</a>
  <a class="abs nav-link" style="left:866px" href="#">PORTFOLIO</a>
</nav>
<a class="btn login" href="#">Log In</a>

<!-- Hero -->
<svg class="abs hero-art" viewBox="0 0 1200 593" role="img" aria-label="Photo of a laptop on a wooden desk in a bright office">
  <defs>
    <linearGradient id="heroTone" x1="0" y1="0" x2="1" y2="1">
      <stop offset="0" stop-color="#d8cdbd"/>
      <stop offset="0.5" stop-color="#b59c80"/>
      <stop offset="1" stop-color="#6e5644"/>
    </linearGradient>
  </defs>
  <path d="M0 0 H1200 V478 C1000 515 700 560 450 588 C300 602 150 565 0 508 Z" fill="url(#heroTone)"/>
</svg>
<div class="abs hero-circle">
  <div class="hero-welcome">WELCOME TO</div>
  <div class="hero-title">BRINDLE.VC</div>
  <p class="hero-text">Brindle.vc is a venture capital firm that invests<br>in innovative seed-stage technology</p>
</div>
<a class="btn hero-cta" href="#">Get Started</a>
<svg class="abs hero-next" width="26" height="40" viewBox="0 0 26 40"><path d="M4 4 L22 20 L4 36" fill="none" stroke="#fff" stroke-width="3"/></svg>

<!-- What we're looking for -->
<div class="abs look-frame"><div class="look-photo" role="img" aria-label="Photo of hands typing on a laptop"></div></div>
<h2 class="abs heading look-title">What We're Looking For</h2>
<p class="abs look-text">Founding Team: Visionary, Committed, Coachable, Skilled, Aligned, With Market Fit Total Addressable Market: Large, Growing, and Attractive; With a Manageable Competitive Landscape Product Market Fit: MVP + Initial Market Validation; Early Revenue and Growth PotentialTiming: Supportive Market Trends; Not Too Early or Too Late, Just Right Problem: Big Pain; Customers Care About It + Are Willing to Pay Customers: Understand Who + How to Reach; Realistic Go to Market</p>
<a class="btn look-cta" href="#">Learn More</a>

<!-- Investments -->
<section class="abs invest"></section>
<h2 class="abs heading invest-title">Our VC Investments</h2>

<div class="abs step" style="left:110px;top:1449px">
  <svg class="step-icon" viewBox="0 0 60 60" fill="none" stroke="#fff" stroke-width="2"><path d="M20 40 C12 34 12 18 30 14 C48 18 48 34 40 40 V46 H20 Z"/><path d="M22 50 H38 M24 54 H36"/><circle cx="30" cy="29" r="6"/><circle cx="30" cy="29" r="10" stroke-dasharray="3 3"/><path d="M30 2 V8 M10 10 L14 14 M50 10 L46 14 M2 28 H8 M52 28 H58"/></svg>
  <div class="step-title">Innovative Technology</div>
  <p class="step-text">We follow up on referrals to<br>innovative technology companies at<br>the pre-seed or seed stage of funding</p>
  <a class="step-more" href="#">Read More &rarr;</a>
</div>
<div class="abs step featured" style="left:443px;top:1449px">
  <svg class="step-icon" viewBox="0 0 60 60" fill="none" stroke="#7d9a31" stroke-width="2"><rect x="6" y="8" width="48" height="34"/><path d="M4 8 H56 M30 42 V54 M22 54 H38 M30 2 V8"/><circle cx="40" cy="25" r="8"/><path d="M40 17 V25 H48"/><path d="M12 16 H26 M12 22 H26 M12 28 H22 M12 34 H26"/></svg>
  <div class="step-title">Presentation</div>
  <p class="step-text">Before meeting, we'll review the<br>company's investor pitch<br>presentation and its website</p>
  <a class="step-more" href="#">Read More &rarr;</a>
</div>
<div class="abs step" style="left:774px;top:1449px">
  <svg class="step-icon" viewBox="0 0 60 60" fill="none" stroke="#fff" stroke-width="2"><circle cx="30" cy="16" r="9"/><path d="M14 44 C14 32 20 28 30 28 C40 28 46 32 46 44"/><rect x="18" y="38" width="24" height="14"/><path d="M6 54 H54"/></svg>
  <div class="step-title">Benefits of Working</div>
  <p class="step-text">Together, we'll discuss the benefits of<br>working with a venture firm and<br>Brindle in particular</p>
  <a class="step-more" href="#">Read More &rarr;</a>
</div>

<div class="abs step" style="left:110px;top:1760px">
  <svg class="step-icon" viewBox="0 0 60 60" fill="none" stroke="#fff" stroke-width="2"><rect x="6" y="4" width="30" height="40"/><path d="M12 12 H30 M12 18 H30 M12 24 H24 M12 30 H26"/><circle cx="42" cy="44" r="12"/><path d="M46 39 C44 37 38 37 38 41 C38 45 46 43 46 47 C46 51 40 51 38 49 M42 34 V54"/></svg>
  <div class="step-title">Financing</div>
  <p class="step-text">If we want to move forward, we'll<br>negotiate the deal structure and<br>financing terms with the founders</p>
  <a class="step-more" href="#">Read More &rarr;</a>
</div>
<div class="abs step" style="left:443px;top:1760px">
  <svg class="step-icon" viewBox="0 0 60 60" fill="none" stroke="#fff" stroke-width="2"><circle cx="36" cy="24" r="10"/><path d="M36 18 V30 M32 21 H39 M33 27 H40"/><path d="M4 46 L16 36 H30 C34 36 34 42 30 42 H22 M30 42 L46 34 C50 32 52 37 48 40 L30 52 H12 L8 56"/><path d="M44 6 L52 2 L50 10"/></svg>
  <div class="step-title">Our Investment</div>
  <p class="step-text">We'll conduct in depth due diligence<br>and draft our investment<br>thesis sheet</p>
  <a class="step-more" href="#">Read More &rarr;</a>
</div>
<div class="abs step" style="left:774px;top:1760px">
  <svg class="step-icon" viewBox="0 0 60 60" fill="none" stroke="#fff" stroke-width="2"><rect x="8" y="4" width="32" height="46"/><path d="M14 12 H34 M14 18 H34 M14 24 H28"/><path d="M26 42 L34 34 H42 L50 40 L44 48 H36 Z"/><path d="M34 40 L40 44"/></svg>
  <div class="step-title">Legal Agreements</div>
  <p class="step-text">Finally, we'll prepare and sign the<br>legal agreements, the investment<br>sheet, and then fund the investment</p>
  <a class="step-more" href="#">Read More &rarr;</a>
</div>
<a class="btn view-all" href="#">View All</a>

<!-- Portfolio -->
<h2 class="abs heading portfolio-title">Brindle Fund I Portfolio</h2>
<div class="abs company" style="left:123px;top:2373px">Brookline</div>
<div class="abs company" style="left:382px;top:2373px"><span class="company-mark"></span>Vantorq</div>
<div class="abs company" style="left:640px;top:2373px">Pellamoor</div>
<div class="abs company" style="left:898px;top:2373px">Keyward</div>
<div class="abs company" style="left:255px;top:2552px">Tessaly</div>
<div class="abs company" style="left:513px;top:2552px">Oprelle</div>
<div class="abs company" style="left:771px;top:2552px">Lumenta</div>
<a class="abs slider-arrow" style="left:53px;top:2539px" href="#" aria-label="Previous"><svg width="20" height="12" viewBox="0 0 20 12"><path d="M19 6 H2 M7 1 L2 6 L7 11" fill="none" stroke="#555" stroke-width="1.6"/></svg></a>
<a class="abs slider-arrow" style="left:1111px;top:2539px" href="#" aria-label="Next"><svg width="20" height="12" viewBox="0 0 20 12"><path d="M1 6 H18 M13 1 L18 6 L13 11" fill="none" stroke="#7d9a31" stroke-width="1.6"/></svg></a>

<!-- Team -->
<svg class="abs team-art" viewBox="0 0 1200 620" aria-hidden="true">
  <defs>
    <linearGradient id="teamTone" x1="0" y1="0" x2="0" y2="1">
      <stop offset="0" stop-color="#6f8d27"/>
      <stop offset="0.6" stop-color="#819f35"/>
      <stop offset="1" stop-color="#6f8d27"/>
    </linearGradient>
  </defs>
  <rect x="0" y="0" width="1200" height="620" fill="url(#teamTone)"/>
  <path d="M0 520 C250 600 500 640 760 580 C950 535 1100 500 1200 505 V620 H0 Z" fill="#000"/>
</svg>
<div class="abs footer-base"></div>
<h2 class="abs heading team-title">Brindle Team</h2>

<div class="abs member" style="left:112px;top:2963px">
  <div class="member-photo" role="img" aria-label="Portrait illustration of Owen Harwick"></div>
  <div class="member-name">Owen Harwick</div>
  <div class="member-role">General Partner, Funds I and II</div>
  <div class="member-links"><span></span><span></span></div>
</div>
<div class="abs member" style="left:361px;top:2963px">
  <div class="member-photo" role="img" aria-label="Portrait illustration of Devan Sorell"></div>
  <div class="member-name">Devan Sorell</div>
  <div class="member-role">General Partner Fund II, Partner Fund I</div>
  <div class="member-links"><span></span><span></span></div>
</div>
<div class="abs member" style="left:610px;top:2963px">
  <div class="member-photo" role="img" aria-label="Portrait illustration of Marla Quenby"></div>
  <div class="member-name">Marla Quenby</div>
  <div class="member-role">General Partner Fund II,&nbsp; Fund I</div>
  <div class="member-links"><span></span><span></span></div>
</div>
<div class="abs member" style="left:860px;top:2963px">
  <div class="member-photo" role="img" aria-label="Portrait illustration of Blair Tennant"></div>
  <div class="member-name">Blair Tennant</div>
  <div class="member-role">Partner Fund I</div>
  <div class="member-links"><span></span><span></span></div>
</div>

<!-- Footer -->
<footer>
  <a class="abs footer-brand" href="#"><span class="brand-dot"></span><span class="brand-name">BRINDLE.VC</span></a>

  <div class="abs footer-head" style="left:357px">Links</div>
  <ul class="abs footer-links">
    <li>Home</li><li>What</li><li>How</li><li>Who</li><li>Portfolio</li>
  </ul>

  <div class="abs footer-head" style="left:478px">Contact Us</div>
  <div class="abs contact-row" style="top:3537px">
    <svg width="16" height="20" viewBox="0 0 16 20" style="margin-top:4px"><path d="M8 19 C3 12 1 9 1 7 A7 7 0 0 1 15 7 C15 9 13 12 8 19 Z" fill="#fff"/><circle cx="8" cy="7" r="2.5" fill="#000"/></svg>
    <span>Lorem ipsum dolor sit<br>amet, consectetur</span>
  </div>
  <div class="abs contact-row" style="top:3606px">
    <svg width="16" height="16" viewBox="0 0 24 24" style="margin-top:3px"><path d="M6.6 10.8a15 15 0 0 0 6.6 6.6l2.2-2.2c.3-.3.7-.4 1-.2 1.1.4 2.3.6 3.6.6.6 0 1 .4 1 1V20c0 .6-.4 1-1 1C10.6 21 3 13.4 3 4c0-.6.4-1 1-1h3.5c.6 0 1 .4 1 1 0 1.3.2 2.5.6 3.6.1.3 0 .7-.2 1z" fill="#fff"/></svg>
    <span>(555) 014 2290</span>
  </div>
  <div class="abs contact-row" style="top:3643px">
    <svg width="16" height="12" viewBox="0 0 16 12" style="margin-top:5px"><rect x="0.5" y="0.5" width="15" height="11" fill="none" stroke="#fff"/><path d="M0.5 0.5 L8 6.5 L15.5 0.5" fill="none" stroke="#fff"/></svg>
    <span>info@brindlevc.com</span>
  </div>

  <div class="abs footer-head" style="left:707px">Follow Us</div>
  <div class="abs follow-row" style="top:3548px"><span class="follow-dot"></span>Gatherly</div>
  <div class="abs follow-row" style="top:3590px"><span class="follow-dot"></span>Quipster</div>
  <div class="abs follow-row" style="top:3633px"><span class="follow-dot"></span>Snapfolio</div>
  <div class="abs follow-row" style="top:3675px"><span class="follow-dot"></span>Linkward</div>

  <div class="abs footer-head" style="left:861px">Newsletter</div>
  <div class="abs news-input">Enter Email</div>
  <a class="btn news-submit" href="#">Submit</a>

  <p class="abs copyright">©Copyrights 2021 Brindlevc &nbsp;|&nbsp;&nbsp; All Rights Reserved</p>
</footer>

</body>
</html>
```